Owen Tasker Studios Business Card

Looking for a clear, modern, elegant, sharp business card that conveys a professional yet edgy image to my business as a wedding, portrait, and travel photographer. Would like something that looks vintage yet modern. Need a new business card to grow my business. We are growing the business for Wedding and Event Photography as well as fine art Photography. (Mostly Landscapes)
Updates

I’m looking through designs now but I have a new logo that i want using please.

New logo uploaded please redesign using that

PLEASE ALL DESIGNERS LOOK IN BRIEF FOR NEW LOGO

Target Market(s)

Brides, Grooms, Families with Kids, People looking for Fine Art Photography Artwork

Industry/Entity Type

Photographer

Contact Information for Business Card

Unsure

Font styles to use
Serif

Colors

Designer to choose colors to be used in the design.

Requirements
Must have
• My Website:
• http://taskerlens.examplefolio.net
• Phone:
• 323-481-5206
• Email:
• owentaskerlens@mailbox-example.net
Nice to have
• Would like a sort of shine on the printing finish.
• I like black I think it looks good on a business card.
• Can try working with my logo (png that I've attached)

```html
<!DOCTYPE html>
<html lang="en">
<head>
<meta charset="utf-8">
<title>Owen Tasker Studios Business Card</title>
<link rel="stylesheet" href="https://fonts.googleapis.com/css2?family=Montserrat:wght@300;400;500&display=swap">
<style>
  :root {
    --page: #2a2a2a;
    --ink: #0a0a0a;
    --paper: #ffffff;
    --silver: #d9d9d9;
    --text-dark: #111111;
  }
  * { margin: 0; padding: 0; box-sizing: border-box; }
  html, body { width: 1200px; height: 900px; overflow: hidden; }
  body {
    background: var(--page);
    font-family: "Montserrat", Arial, sans-serif;
    position: relative;
  }
  .card {
    position: absolute;
    left: 290px;
    width: 620px;
    height: 354px;
    overflow: hidden;
    box-shadow: 0 10px 24px rgba(0,0,0,0.45);
  }
  .card--front { top: 70px; background: var(--ink); }
  .card--back { top: 476px; background: var(--paper); }

  /* Front */
  .front-frame {
    position: absolute;
    left: 120px; top: 42px;
    width: 228px; height: 270px;
    border: 3px solid var(--silver);
  }
  .brand {
    position: absolute;
    color: var(--silver);
    font-weight: 300;
    text-align: center;
    line-height: 1;
  }
  .brand__name { display: block; font-size: 26px; letter-spacing: 0.5px; }
  .brand__sub { display: block; font-size: 12px; letter-spacing: 9px; margin-top: 6px; padding-left: 9px; }
  .card--front .brand { left: 330px; top: 64px; }

  /* Back */
  .back-top {
    position: absolute; left: 0; top: 0;
    width: 620px; height: 168px;
    background: var(--ink);
  }
  .card--back .brand { left: 0; width: 620px; top: 72px; color: var(--paper); }
  .card--back .brand__name { font-size: 30px; }
  .card--back .brand__sub { font-size: 13px; letter-spacing: 10px; }
  .rule { position: absolute; height: 5px; background: var(--ink); }
  .rule--left { left: 0; top: 202px; width: 228px; }
  .rule--right { left: 392px; top: 178px; width: 228px; }
  .rule--bottom { left: 0; top: 258px; width: 300px; }
  .holder {
    position: absolute; left: 0; width: 620px; top: 184px;
    text-align: center; color: var(--text-dark);
    font-size: 11.5px; line-height: 1.35; font-weight: 400;
  }
  .holder__name { letter-spacing: 0.6px; }
  .icon-block {
    position: absolute; left: 22px; top: 268px;
    width: 60px; height: 86px;
    background: var(--ink);
  }
  .icon-block svg { position: absolute; left: 22px; width: 16px; height: 16px; }
  .contact {
    position: absolute; left: 100px; top: 272px;
    list-style: none; color: var(--text-dark);
    font-size: 13.5px; line-height: 21px;
  }
</style>
</head>
<body>
  <section class="card card--front" aria-label="Card front">
    <div class="front-frame"></div>
    <div class="brand">
      <span class="brand__name">OWEN TASKER</span>
      <span class="brand__sub">STUDIOS</span>
    </div>
  </section>

  <section class="card card--back" aria-label="Card back">
    <div class="back-top"></div>
    <div class="brand">
      <span class="brand__name">OWEN TASKER</span>
      <span class="brand__sub">STUDIOS</span>
    </div>
    <div class="rule rule--right"></div>
    <div class="rule rule--left"></div>
    <div class="holder">
      <div class="holder__name">MARCUS HALE</div>
      <div class="holder__role">Photographer</div>
    </div>
    <div class="rule rule--bottom"></div>
    <div class="icon-block">
      <svg style="top:10px" viewBox="0 0 16 16" aria-hidden="true">
        <path d="M4 2 L6 2 L7 5 L5.5 6.2 Q7 9.2 9.8 10.5 L11 9 L14 10 L14 12 Q14 14 12 14 Q3 13 2 4 Q2 2 4 2 Z" fill="#fff"/>
      </svg>
      <svg style="top:35px" viewBox="0 0 16 16" aria-hidden="true">
        <rect x="2" y="4" width="12" height="8.5" fill="#fff"/>
        <path d="M2 4 L8 9 L14 4" fill="none" stroke="#0a0a0a" stroke-width="1.2"/>
      </svg>
      <svg style="top:60px" viewBox="0 0 16 16" aria-hidden="true">
        <g fill="none" stroke="#fff" stroke-width="1.2">
          <circle cx="8" cy="8" r="6"/>
          <ellipse cx="8" cy="8" rx="2.6" ry="6"/>
          <line x1="2" y1="8" x2="14" y2="8"/>
        </g>
      </svg>
    </div>
    <ul class="contact">
      <li>323-481-5206</li>
      <li>owentaskerlens@mailbox-example.net</li>
      <li>http://taskerlens.examplefolio.net</li>
    </ul>
  </section>
</body>
</html>
```